School Canteen Menu

We operate 30 school canteen/cafes across Melbourne. We are looking to update our old menu to a new attractive design.
We offer a variety of both food and drink and we need to highlight our healthy options. We would like to have a background picture of either salads or healthy sandwiche etc.
We have borken our current menu in catogories according to hot food, cold bar, drinks, ice creams etc.
We would prefer it to be a A4 design but other ideas are welcome.

In summary we need a vibrant attractive applealing design.
My business card with our lgo is also attached
Regards

Tam

We have two types of menu a secondary menu for students 12-18 and a primary school menu 5-12 year olds. I have attached samples of both.

Target Market(s)

12 year old to 18 year olds. School Students. As well as Teachers. Prehaps encouraging Teaches with our Freshly made salads will be a feature.

Industry/Entity Type

School

Requirements
Must have
• Viabrant Colors. Greens, Purples, Yellows.
Should not have
• Red Colors. Considered to be a unhealthy color.

```html
<!DOCTYPE html>
<html lang="en">
<head>
<meta charset="utf-8">
<title>Canteen Menu 2012</title>
<link href="https://fonts.googleapis.com/css2?family=Chewy&family=PT+Sans:wght@400;700&display=swap" rel="stylesheet">
<style>
  :root{
    --leaf-dark:#2f7d1e;
    --leaf:#4aa52c;
    --leaf-light:#9fd36b;
    --text-green:#2b7a22;
    --sun:#f7d417;
    --sun-deep:#e9b800;
    --panel:#ffffff;
    --band:#3f8f1f;
  }
  *{box-sizing:border-box;margin:0;padding:0}
  html,body{width:1200px;height:855px;overflow:hidden;background:#ffffff}
  body{font-family:"PT Sans",sans-serif;color:var(--text-green)}
  .menu{position:relative;width:1200px;height:855px;
    background:radial-gradient(ellipse at 30% 40%,#d9f0b0 0%,#8fcb5a 45%,#4f9f2a 100%);
    overflow:hidden}
  .backdrop-photo{position:absolute;inset:0;
    background:radial-gradient(circle at 12% 70%,rgba(255,255,255,.35),transparent 30%),
               radial-gradient(circle at 85% 75%,rgba(230,120,150,.28),transparent 30%),
               radial-gradient(circle at 55% 10%,rgba(255,255,255,.25),transparent 35%)}
  .title{position:absolute;top:36px;left:0;width:1200px;text-align:center;
    font-family:"Chewy",cursive;font-weight:400;font-size:54px;line-height:60px;color:var(--sun);letter-spacing:3px;
    text-shadow:2px 3px 0 var(--leaf-dark)}
  .milk-photo{position:absolute;left:70px;top:58px;width:52px;height:105px;border-radius:6px;
    background:linear-gradient(180deg,#f3f3f3 0%,#c9a0b4 35%,#8e5570 100%)}
  .sandwich-photo{position:absolute;left:1010px;top:18px;width:150px;height:120px;border-radius:50% 45% 40% 50%;
    background:radial-gradient(ellipse at 50% 50%,#f1d9a0 0%,#d9a65a 55%,#8bbd4a 80%,transparent 82%)}
  .panel{position:absolute;top:114px;height:640px;background:var(--panel);border-radius:12px;
    padding:8px 16px;box-shadow:0 2px 6px rgba(0,0,0,.2);overflow:hidden}
  .col-hot{left:56px;width:350px}
  .col-salad{left:416px;width:338px}
  .col-snacks{left:764px;width:350px}
  h2{font-family:"Chewy",cursive;font-weight:400;font-size:36px;color:var(--leaf);text-align:center;line-height:40px}
  .row{display:flex;justify-content:space-between;font-weight:700;font-size:13.5px;line-height:16.5px}
  .row .note{font-weight:400}
  .sub{font-size:12px;line-height:16px;font-weight:700}
  .gap{height:11px}
  .dot{display:inline-block;width:13px;height:13px;border-radius:50%;background:var(--sun);
    border:1px solid var(--sun-deep);vertical-align:-2px;margin-left:4px}
  .indent{padding-left:108px;padding-right:60px}
  .jaffle-row{position:relative;height:20px;align-items:flex-end}
  .jaffle-label{position:absolute;left:110px;bottom:0;font-family:"Chewy",cursive;font-weight:400;font-size:21px;line-height:22px;color:var(--leaf)}
  .section-label{font-family:"Chewy",cursive;font-weight:400;font-size:19px;line-height:22px;color:var(--leaf-dark)}
  .wrap-band{background:linear-gradient(90deg,#e6f3d7,#ffffff)}
  .notice{position:absolute;left:0;right:0;bottom:10px;margin:0 8px;background:var(--band);color:#fff;
    border-radius:6px;padding:12px 10px 8px;text-align:center;font-weight:700;font-size:14.5px;line-height:19px}
  .notice .green{color:var(--leaf-light)}
  .notice .dot{position:absolute;top:-13px;left:50%;margin-left:-11px;width:22px;height:22px}
  .closed{position:absolute;top:766px;left:0;width:1200px;height:34px;text-align:center;
    background:linear-gradient(90deg,transparent,rgba(47,125,30,.85) 20%,rgba(47,125,30,.85) 80%,transparent);
    font-family:"Chewy",cursive;font-weight:400;font-size:24px;line-height:34px;color:var(--sun);letter-spacing:1px}
</style>
</head>
<body>
<div class="menu">
  <div class="backdrop-photo" role="img" aria-label="Background photo of fresh salad greens"></div>
  <div class="milk-photo" role="img" aria-label="Photo of a flavoured milk carton"></div>
  <div class="sandwich-photo" role="img" aria-label="Photo of a fresh salad sandwich"></div>
  <h1 class="title">Canteen Menu 2012</h1>

  <section class="panel col-hot">
    <h2>Hot Food</h2>
    <div class="row jaffle-row"><span>Cheese</span><span class="jaffle-label">Jaffles</span><span>$2.50</span></div>
    <div class="row"><span>Spaghetti <i class="dot"></i></span><span>$2.50</span></div>
    <div class="row"><span>Baked Beans <i class="dot"></i></span><span>$2.50</span></div>
    <div class="row"><span>Ham &amp; Cheese</span><span>$2.60</span></div>
    <div class="row"><span>Ham, Cheese &amp; Pineapple</span><span>$3.00</span></div>
    <div class="gap"></div>
    <div class="row"><span>Lasagne 97% Fat Free <i class="dot"></i></span><span>$3.60</span></div>
    <div class="row"><span>Macaroni &amp; Cheese 97% Fat Free <i class="dot"></i></span><span>$3.60</span></div>
    <div class="row"><span>Meat Pie</span><span>$3.20</span></div>
    <div class="row"><span>Party Pie or Party Sausage Roll</span><span>$1.00</span></div>
    <div class="row"><span>Sausage Roll</span><span>$3.00</span></div>
    <div class="gap"></div>
    <div class="row"><span>Flame Grilled Beef Burger <i class="dot"></i></span><span>$4.00</span></div>
    <div class="row"><span>with lettuce, cheese and tomato</span></div>
    <div class="row"><span>Chicken Burger</span></div>
    <div class="row"><span>with lettuce, cheese &amp; mayonnaise</span><span>$4.00</span></div>
    <div class="row"><span>Baked Chicken Schnitzel Roll</span></div>
    <div class="row"><span>with lettuce, cheese, tomato &amp; mayo</span><span>$4.20</span></div>
    <div class="gap"></div>
    <div class="row"><span>Corn Cobette <i class="dot"></i></span><span>$1.20</span></div>
    <div class="row"><span>Noodles - Chicken or Beef</span><span>$2.60</span></div>
    <div class="row"><span>Chicken Nuggets 80c each</span><span>(3) $2.20</span></div>
    <div class="row"><span>Steamed Dim Sim</span><span>$0.90</span></div>
    <div class="row"><span>Hot Dog</span><span>$3.00</span></div>
    <h2 style="margin:10px 0 12px">Specials</h2>
    <div class="row"><span>Health Pack 1</span></div>
    <div class="row"><span class="note">Salad Roll, Cookie &amp; 200ml Fruit Box</span><span>$6.00</span></div>
    <div class="gap"></div>
    <div class="row"><span>Health Pack 2</span></div>
    <div class="row"><span class="note">Any 97% Fat Free Pasta, 300ml</span></div>
    <div class="row"><span class="note">Flavoured Milk (FRESH)</span><span>$6.00</span></div>
  </section>

  <section class="panel col-salad">
    <h2>Salad Plates</h2>
    <div class="section-label">Salad Plates</div>
    <div class="sub">all with lettuce, cucumber, carrot, tomato &amp; beetroot</div>
    <div style="height:6px"></div>
    <div class="indent">
      <div class="row"><span>Salad <i class="dot"></i></span><span>$3.40</span></div>
      <div class="row"><span>Egg <i class="dot"></i></span><span>$3.60</span></div>
      <div class="row"><span>Chicken <i class="dot"></i></span><span>$3.90</span></div>
      <div class="row"><span>Cheese</span><span>$3.60</span></div>
      <div class="row"><span>Ham <i class="dot"></i></span><span>$3.60</span></div>
      <div class="row"><span>Tuna <i class="dot"></i></span><span>$3.60</span></div>
    </div>
    <h2 style="margin-top:8px">Sandwiches</h2>
    <div class="row" style="justify-content:flex-start;align-items:baseline"><span class="section-label">Sandwiches</span><span class="note" style="font-size:12px;margin-left:12px"><b>Rolls</b> 60c extra</span></div>
    <div style="padding-left:18px">
      <div class="row"><span>Salad <i class="dot"></i></span></div>
      <div class="row"><span class="note" style="font-size:12px">lettuce, tomato, carrot, beetroot, cucumber</span><span>$2.80</span></div>
      <div style="height:7px"></div>
      <div class="row"><span>Ham &amp; Tomato <i class="dot"></i></span><span>$2.40</span></div>
      <div class="row"><span>Ham, Cheese &amp; Tomato <i class="dot"></i></span><span>$2.60</span></div>
      <div class="row"><span>Cheese &amp; Tomato <i class="dot"></i></span><span>$2.40</span></div>
      <div class="row"><span>Cheese &amp; Salad <i class="dot"></i></span><span>$3.00</span></div>
      <div class="row"><span>Egg &amp; Lettuce <i class="dot"></i></span><span>$2.80</span></div>
      <div class="row"><span>Chicken &amp; Salad <i class="dot"></i></span><span>$3.10</span></div>
      <div class="row"><span>Tuna &amp; Tomato <i class="dot"></i></span><span>$2.90</span></div>
      <div class="row"><span>Tuna, Lettuce &amp; Mayonnaise</span><span>$3.00</span></div>
      <div class="row"><span>Yeast Spread</span><span>$1.60</span></div>
      <div class="row"><span>Ham</span><span>$2.20</span></div>
      <div class="row"><span>extra fillings</span><span>$0.40</span></div>
    </div>
    <h2 style="margin-top:6px;font-size:30px;line-height:34px">Wraps</h2>
    <div class="wrap-band">
      <div class="row"><span>BBQ Chicken</span></div>
      <div class="row"><span class="note">Chicken, Lettuce, BBQ Sauce</span><span>$3.60</span></div>
      <div class="row"><span>Sweet Chilli Chicken</span></div>
      <div class="row"><span class="note">Chicken, Lettuce, Sweet Chilli Sauce</span><span>$3.60</span></div>
    </div>
  </section>

  <section class="panel col-snacks">
    <h2 style="text-align:left;padding-left:4px">Snacks</h2>
    <div style="height:10px"></div>
    <div class="row"><span>Pikelets <i class="dot"></i></span><span>$0.80</span></div>
    <div class="row"><span>Pop Corn <i class="dot"></i></span><span>$2.00</span></div>
    <div class="row"><span>Fruit Salad – small <i class="dot"></i></span><span>$1.50</span></div>
    <div class="row"><span>Fruit of the day <i class="dot"></i></span><span>$0.80</span></div>
    <div class="row"><span>Jelly Cup with Fruit</span><span>$1.50</span></div>
    <div class="row"><span>Anzac Cookie</span><span>$2.00</span></div>
    <div class="row"><span>Mini Muffins (home baked)</span><span>$0.80</span></div>
    <h2 style="margin:16px 0 14px">Drinks</h2>
    <div class="row"><span>Flavoured Milk (300ml)</span><span>$2.50</span></div>
    <div class="row"><span>Chocolate, Strawberry,</span></div>
    <div class="row"><span>Iced Coffee (FRESH)</span></div>
    <div class="gap"></div>
    <div class="row"><span>Water (600ml) <i class="dot"></i></span><span>$2.30</span></div>
    <div class="row"><span>Fruit Juice (200ml) Tropical,</span></div>
    <div class="row"><span>Orange, Apple</span><span>$1.50</span></div>
    <h2 style="margin:24px 0 16px">Ice Creams</h2>
    <div class="row"><span>Frozen Orange Wedge <i class="dot"></i></span><span>$0.20</span></div>
    <div class="row"><span>Frozen Pineapple Ring <i class="dot"></i></span><span>$0.50</span></div>
    <div class="row"><span>Frozen Fruit Yoghurt</span><span>$2.00</span></div>
    <div class="row"><span>Zippy Freezer</span><span>$0.80</span></div>
    <div class="row"><span>Sunny Cup Orange, Lemonade</span><span>$2.00</span></div>
    <div class="notice"><i class="dot"></i>Foods marked with a smiley are <span class="green">green foods</span> and can be eaten everyday</div>
  </section>

  <div class="closed">Canteen Closed on Tuesdays &amp; Wednesday's</div>
</div>
</body>
</html>
```